Brochure Design Project for Folk High School in Norway

We're a Folk High School placed in the south of Norway. We want help in creating a new brochure for our school next year. Check this link for the brochure for current year: http://www.brennvikskole.no/db/repository/x58301746290385716204937.pdf

We want a new design. It should not be larger than A4 size. The design dosen't need to be quadratic.

As a starting, the borchure should contain the same amount of pages and information as current brochure.

We also want access to the working-file (InDesign). We've got a lot of pictures to use, so the design template could contain more pictures.

This is a School for students in the agegroup between 18-20 years. The design must attract this group. It's a 1-year study and our focus is to give the students qualified teaching in their area of interest and great experiences linked to travelling, friendship and personal development.

As a starter, we want to see a template on a modern, playful,warm and attractive brochure. This could be shown as a PDF-file.
Updates

You can follow this link to choose among several pictures:

http://www.pixmora.example/photos/41572038@N09/

I remind you that we want access to de InDesign file... So the choose of pictures is not that important. We want for ourselves to change them. If you follow the link, you''ll find compressed pictures. But maybe they can help you in the creative process... :) We''re looking forward to see your work!

```html
<!DOCTYPE html>
<html lang="no">
<head>
<meta charset="utf-8">
<title>Musikk – brosjyreoppslag</title>
<link rel="stylesheet" href="https://fonts.googleapis.com/css2?family=Arvo:wght@400;700&display=swap">
<style>
  :root{
    --canvas:#ffffff;
    --yellow:#f3df74;
    --red:#c4161c;
    --black:#0a0a0a;
    --white:#ffffff;
    --dark:#111111;
  }
  *{box-sizing:border-box;margin:0;padding:0}
  html,body{width:765px;height:1200px;overflow:hidden;background:var(--canvas)}
  body{position:relative;font-family:"Arvo",Georgia,serif}

  .spread{position:absolute;left:37px;width:693px;height:345px;box-shadow:1px 2px 4px rgba(0,0,0,.35);overflow:hidden}
  .spread--night{top:33px;--page:var(--black);--ink:var(--white);--head:var(--yellow);--band:var(--yellow);--band-ink:var(--dark);--accent:var(--yellow)}
  .spread--paper{top:423px;--page:var(--white);--ink:var(--dark);--head:var(--red);--band:var(--red);--band-ink:var(--white);--accent:var(--red)}
  .spread--scarlet{top:817px;--page:var(--red);--ink:var(--white);--head:var(--white);--band:var(--white);--band-ink:var(--dark);--accent:var(--dark)}

  .page-left{position:absolute;left:0;top:0;width:346px;height:345px;background:#1a1410}
  .page-right{position:absolute;left:346px;top:0;width:347px;height:345px;background:var(--page);color:var(--ink)}

  .photo{position:absolute}
  .photo--piano{left:0;top:0;width:116px;height:97px;background:linear-gradient(90deg,#e9e6e0 0%,#b9b3aa 35%,#3a2e26 70%,#2a211c 100%)}
  .photo--drums{left:116px;top:0;width:115px;height:97px;background:radial-gradient(circle at 40% 60%,#4a4a4a 0%,#1b1b1b 45%,#6e1010 80%,#8d1a15 100%)}
  .photo--keys{left:231px;top:0;width:115px;height:97px;background:linear-gradient(180deg,#1d2f7a 0%,#3e3a6a 40%,#1a1a1a 100%)}
  .photo--guitar{left:0;top:108px;width:346px;height:237px;background:radial-gradient(ellipse at 48% 42%,#ffd27a 0%,#f08a24 18%,#8a3a10 40%,#2a1a12 65%,#14100d 100%)}

  .band{position:absolute;left:0;top:97px;width:505px;height:11px;background:var(--band)}

  .brand{position:absolute;right:12px;top:14px;display:flex;align-items:center;gap:4px;color:var(--head);font-weight:700;font-size:7px;letter-spacing:.3px}
  .brand-mark{width:14px;height:14px;background:var(--head)}

  .title{position:absolute;left:50px;top:50px;color:var(--head);font-weight:700;font-size:29px;line-height:1;letter-spacing:.5px}
  .subtitle{position:absolute;left:50px;top:80px;color:var(--head);font-weight:700;font-size:10.5px;letter-spacing:.2px}
  .spread--night .subtitle{color:var(--white)}
  .spread--paper .subtitle{color:var(--dark)}

  .intro{position:absolute;left:-10px;top:98px;width:190px;display:flex;flex-direction:column;align-items:flex-end;font-weight:700;font-size:6.4px;line-height:8.6px}
  .intro span{background:var(--band);color:var(--band-ink);padding:0 3px;white-space:nowrap}

  .col{position:absolute;top:162px;font-size:4.6px;line-height:6.2px}
  .col p{margin-bottom:5px}
  .col ul{list-style:none;margin-bottom:5px}
  .col li{margin-bottom:1.5px}
  .col li::before{content:"• "}
  .col--one{left:28px;width:96px}
  .col--two{left:132px;width:96px}
  .col--facts{left:246px;width:80px;border-left:1px dotted var(--accent);padding-left:8px;top:162px}
  .hl{color:var(--accent);font-weight:700}
  .facts-title{color:var(--accent);font-weight:700;font-size:6px;margin-bottom:2px}

  .folio{position:absolute;bottom:5px;font-size:5px;font-weight:700;color:var(--white)}
  .folio--left-num{left:4px}
  .folio--phone{left:262px}
  .page-right .folio{color:var(--ink)}
  .folio--web{left:28px}
  .folio--right-num{right:12px}
</style>
</head>
<body>

<section class="spread spread--night">
  <div class="page-left">
    <div class="photo photo--piano" role="img" aria-label="Elev som spiller piano"></div>
    <div class="photo photo--drums" role="img" aria-label="Elev bak trommesettet"></div>
    <div class="photo photo--keys" role="img" aria-label="Elev ved keyboard"></div>
    <div class="photo photo--guitar" role="img" aria-label="Gitarist i varmt scenelys"></div>
    <span class="folio folio--left-num">12</span>
    <span class="folio folio--phone">TELEFON 31 64 20 50</span>
  </div>
  <div class="band"></div>
  <div class="page-right">
    <div class="brand"><span class="brand-mark"></span>BRENNVIK</div>
    <h1 class="title">MUSIKK</h1>
    <h2 class="subtitle">– DITT TALENT, VÅR BEGEISTRING</h2>
    <div class="intro">
      <span>Ønsker du et år med mye tid til å jobbe med</span>
      <span>musikk? På Musikk står du og dine ønsker i fokus.</span>
      <span>Vi tilbyr bandrom, musikkstudio, instru- menter</span>
      <span>og dyktige lærere, - alt lagt til rette for et spennende</span>
      <span>og lærerikt år. Musikkfeltet spenner vidt, du</span>
      <span>velger selv hva du vil bli flin- kere til.</span>
    </div>
    <div class="col col--one">
      <p>Du er selv med og bestemmer program- met, - bli en del av det. Det blir masse spilling og øving, - vi vil jo bli bedre! Vi legger til rette for gode musikkopplevelser:</p>
      <ul><li>Fokus på vokal, - bli en bedre sanger</li><li>Lær å kompe deg selv på piano og gitar</li><li>Få hjelp til vokalinn- spilling</li><li>Spill inn dine egne låter</li></ul>
      <p>Vi har et spesialkonstru- ert tonoms lydstudio med høy kvalitet og moderne arbeidsverktøy. En ny Studiomaskin og Lydverk 9 gir mange muligheter. Vi lærer deg gjerne å bruke et lydstudio! Musikk gir gode mulig- heter for samspill og performance. Musikk og folkehøgskole er perfect match! Ditt talent blir satt pris på. Vår årlige <span class="hl">musikal</span> vil verdsette dine kvaliteter.</p>
    </div>
    <div class="col col--two">
      <p>Studieturen til <span class="hl">New York</span> vil gi deg musikk- opplevelser du sent vil glemme. Musikalske innslag i skolens nærom- råder, inkludert Havnescenen i Kristiansand og diverse musikkfestivaler, vil også utvide din musikalske erfaring. Vi har etablert samarbeid med rytmisk linje på musikkonserva- toriet i Kristiansand. På Musikk får du et spennende år med ba- lanse mellom morsomme utfordringer og sterke opplevelser. Vi hjelper deg å finne kvalifisert lærer til ditt hovedinstrument om du ønsker det. (Tillegg i pris.) Dersom du har eget instrument, tar du det med!</p>
      <p>Linjekostnader: ca. 17 000 kroner</p>
    </div>
    <div class="col col--facts">
      <p class="facts-title">FAGFORDELING</p>
      <p>Linjefag (10-12 t/u)</p>
      <ul><li>Formidling</li><li>Samspill</li><li>Musikkteori</li><li>Låtskriving og arrangering</li><li>Gehør og besifringsspill</li><li>Arbeid i studio</li><li>Performance</li></ul>
      <p>Fellesfag 9 t/u<br>Seminar 4 t/u<br>Valgfag 2-6 t/u</p>
    </div>
    <span class="folio folio--web">WWW.BRENNVIKSKOLE.NO</span>
    <span class="folio folio--right-num">13</span>
  </div>
</section>

<section class="spread spread--paper">
  <div class="page-left">
    <div class="photo photo--piano" role="img" aria-label="Elev som spiller piano"></div>
    <div class="photo photo--drums" role="img" aria-label="Elev bak trommesettet"></div>
    <div class="photo photo--keys" role="img" aria-label="Elev ved keyboard"></div>
    <div class="photo photo--guitar" role="img" aria-label="Gitarist i varmt scenelys"></div>
    <span class="folio folio--left-num">12</span>
    <span class="folio folio--phone">TELEFON 31 64 20 50</span>
  </div>
  <div class="band"></div>
  <div class="page-right">
    <div class="brand"><span class="brand-mark"></span>BRENNVIK</div>
    <h1 class="title">MUSIKK</h1>
    <h2 class="subtitle">– DITT TALENT, VÅR BEGEISTRING</h2>
    <div class="intro">
      <span>Ønsker du et år med mye tid til å jobbe med</span>
      <span>musikk? På Musikk står du og dine ønsker i fokus.</span>
      <span>Vi tilbyr bandrom, musikkstudio, instru- menter</span>
      <span>og dyktige lærere, - alt lagt til rette for et spennende</span>
      <span>og lærerikt år. Musikkfeltet spenner vidt, du</span>
      <span>velger selv hva du vil bli flin- kere til.</span>
    </div>
    <div class="col col--one">
      <p>Du er selv med og bestemmer program- met, - bli en del av det. Det blir masse spilling og øving, - vi vil jo bli bedre! Vi legger til rette for gode musikkopplevelser:</p>
      <ul><li>Fokus på vokal, - bli en bedre sanger</li><li>Lær å kompe deg selv på piano og gitar</li><li>Få hjelp til vokalinn- spilling</li><li>Spill inn dine egne låter</li></ul>
      <p>Vi har et spesialkonstru- ert tonoms lydstudio med høy kvalitet og moderne arbeidsverktøy. En ny Studiomaskin og Lydverk 9 gir mange muligheter. Vi lærer deg gjerne å bruke et lydstudio! Musikk gir gode mulig- heter for samspill og performance. Musikk og folkehøgskole er perfect match! Ditt talent blir satt pris på. Vår årlige <span class="hl">musikal</span> vil verdsette dine kvaliteter.</p>
    </div>
    <div class="col col--two">
      <p>Studieturen til <span class="hl">New York</span> vil gi deg musikk- opplevelser du sent vil glemme. Musikalske innslag i skolens nærom- råder, inkludert Havnescenen i Kristiansand og diverse musikkfestivaler, vil også utvide din musikalske erfaring. Vi har etablert samarbeid med rytmisk linje på musikkonserva- toriet i Kristiansand. På Musikk får du et spennende år med ba- lanse mellom morsomme utfordringer og sterke opplevelser. Vi hjelper deg å finne kvalifisert lærer til ditt hovedinstrument om du ønsker det. (Tillegg i pris.) Dersom du har eget instrument, tar du det med!</p>
      <p>Linjekostnader: ca. 17 000 kroner</p>
    </div>
    <div class="col col--facts">
      <p class="facts-title">FAGFORDELING</p>
      <p>Linjefag (10-12 t/u)</p>
      <ul><li>Formidling</li><li>Samspill</li><li>Musikkteori</li><li>Låtskriving og arrangering</li><li>Gehør og besifringsspill</li><li>Arbeid i studio</li><li>Performance</li></ul>
      <p>Fellesfag 9 t/u<br>Seminar 4 t/u<br>Valgfag 2-6 t/u</p>
    </div>
    <span class="folio folio--web">WWW.BRENNVIKSKOLE.NO</span>
    <span class="folio folio--right-num">13</span>
  </div>
</section>

<section class="spread spread--scarlet">
  <div class="page-left">
    <div class="photo photo--piano" role="img" aria-label="Elev som spiller piano"></div>
    <div class="photo photo--drums" role="img" aria-label="Elev bak trommesettet"></div>
    <div class="photo photo--keys" role="img" aria-label="Elev ved keyboard"></div>
    <div class="photo photo--guitar" role="img" aria-label="Gitarist i varmt scenelys"></div>
    <span class="folio folio--left-num">12</span>
    <span class="folio folio--phone">TELEFON 31 64 20 50</span>
  </div>
  <div class="band"></div>
  <div class="page-right">
    <div class="brand"><span class="brand-mark"></span>BRENNVIK</div>
    <h1 class="title">MUSIKK</h1>
    <h2 class="subtitle">– DITT TALENT, VÅR BEGEISTRING</h2>
    <div class="intro">
      <span>Ønsker du et år med mye tid til å jobbe med</span>
      <span>musikk? På Musikk står du og dine ønsker i fokus.</span>
      <span>Vi tilbyr bandrom, musikkstudio, instru- menter</span>
      <span>og dyktige lærere, - alt lagt til rette for et spennende</span>
      <span>og lærerikt år. Musikkfeltet spenner vidt, du</span>
      <span>velger selv hva du vil bli flin- kere til.</span>
    </div>
    <div class="col col--one">
      <p>Du er selv med og bestemmer program- met, - bli en del av det. Det blir masse spilling og øving, - vi vil jo bli bedre! Vi legger til rette for gode musikkopplevelser:</p>
      <ul><li>Fokus på vokal, - bli en bedre sanger</li><li>Lær å kompe deg selv på piano og gitar</li><li>Få hjelp til vokalinn- spilling</li><li>Spill inn dine egne låter</li></ul>
      <p>Vi har et spesialkonstru- ert tonoms lydstudio med høy kvalitet og moderne arbeidsverktøy. En ny Studiomaskin og Lydverk 9 gir mange muligheter. Vi lærer deg gjerne å bruke et lydstudio! Musikk gir gode mulig- heter for samspill og performance. Musikk og folkehøgskole er perfect match! Ditt talent blir satt pris på. Vår årlige <span class="hl">musikal</span> vil verdsette dine kvaliteter.</p>
    </div>
    <div class="col col--two">
      <p>Studieturen til <span class="hl">New York</span> vil gi deg musikk- opplevelser du sent vil glemme. Musikalske innslag i skolens nærom- råder, inkludert Havnescenen i Kristiansand og diverse musikkfestivaler, vil også utvide din musikalske erfaring. Vi har etablert samarbeid med rytmisk linje på musikkonserva- toriet i Kristiansand. På Musikk får du et spennende år med ba- lanse mellom morsomme utfordringer og sterke opplevelser. Vi hjelper deg å finne kvalifisert lærer til ditt hovedinstrument om du ønsker det. (Tillegg i pris.) Dersom du har eget instrument, tar du det med!</p>
      <p>Linjekostnader: ca. 17 000 kroner</p>
    </div>
    <div class="col col--facts">
      <p class="facts-title">FAGFORDELING</p>
      <p>Linjefag (10-12 t/u)</p>
      <ul><li>Formidling</li><li>Samspill</li><li>Musikkteori</li><li>Låtskriving og arrangering</li><li>Gehør og besifringsspill</li><li>Arbeid i studio</li><li>Performance</li></ul>
      <p>Fellesfag 9 t/u<br>Seminar 4 t/u<br>Valgfag 2-6 t/u</p>
    </div>
    <span class="folio folio--web">WWW.BRENNVIKSKOLE.NO</span>
    <span class="folio folio--right-num">13</span>
  </div>
</section>

</body>
</html>
```